Build With Sisters, 2019 Save The Date

Please develop a save the date flyer our 4th Annual Build With Sisters and See Them Soar! This event is focused on maintaining participation and appreciation for women in the design and construction industry.

This unique Forum provides a venue to engage everyone from executives to those just beginning their careers with active, hands-on sessions and vibrant networking with the best and brightest in the A/E/C industry. In our usual Q-MarTO Forum style, Keynotes become table participants and table participants become presenters, encouraging participants to assimilate what they are learning. Join local, state and national leaders and subject matter experts as we candidly explore and address the issues affecting women in our industry.

Industry/Entity Type

Construction

Font styles to use
Sans Serif

Requirements
Must have
• This is a save the date, Must have:
• Q-MarTO Logo
• Title: 4th Annual Build With Sisters and See Them Soar!
• Date: January 25, 2019
• Location: Larkhaven Ridge Resort and Spa, San Marcos, TX
Nice to have
• A header that can easily be pulled to add to other marketing materials and for use across other platforms (web, etc.).

```html
<!DOCTYPE html>
<html lang="en">
<head>
<meta charset="utf-8">
<title>Build With Sisters – Save The Date 2019</title>
<link rel="stylesheet" href="https://fonts.googleapis.com/css2?family=Cinzel:wght@400;700;900&family=Amatic+SC:wght@400&family=Cormorant+SC:wght@500&display=swap">
<style>
  :root {
    --stage: #d3d3d5;
    --paper: #ffffff;
    --ink: #121212;
    --navy: #2f3d8c;
    --crimson: #c7323b;
    --frame: #3a3a3a;
  }
  * { margin: 0; padding: 0; box-sizing: border-box; }
  html, body {
    width: 1200px; height: 960px; overflow: hidden;
    background: var(--stage);
  }
  .flyer {
    position: absolute; left: 290px; top: 40px;
    width: 620px; height: 880px;
    background: var(--paper);
    overflow: hidden;
    box-shadow: 0 6px 24px rgba(0,0,0,.18);
  }
  .watercolor-wash {
    position: absolute; left: 0; top: 0; width: 100%; height: 420px;
    background:
      radial-gradient(ellipse 40% 35% at 55% 35%, rgba(154,106,184,.85), rgba(154,106,184,0) 70%),
      radial-gradient(ellipse 30% 30% at 30% 25%, rgba(170,120,200,.7), rgba(170,120,200,0) 70%),
      radial-gradient(ellipse 35% 40% at 8% 30%, rgba(228,104,154,.85), rgba(228,104,154,0) 70%),
      radial-gradient(ellipse 35% 40% at 95% 25%, rgba(228,104,154,.8), rgba(228,104,154,0) 70%),
      linear-gradient(to bottom, rgba(220,130,180,.6), rgba(255,255,255,0) 95%);
  }
  .frame {
    position: absolute; inset: 34px 30px 30px 30px;
    border: 1.5px solid var(--frame);
  }
  .frame::after {
    content: ""; position: absolute; inset: 6px;
    border: 1px solid var(--frame); opacity: .5;
  }
  .content { position: absolute; inset: 0; text-align: center; color: var(--ink); }
  .invite-line {
    position: absolute; top: 110px; width: 100%;
    font: 700 12px/1 "Cinzel", serif; letter-spacing: .02em;
  }
  .edition {
    position: absolute; top: 128px; width: 100%;
    font: 700 22px/1 "Cinzel", serif;
  }
  .event-title {
    position: absolute; top: 170px; width: 100%;
    font-family: "Cinzel", serif; font-weight: 900; line-height: 1;
  }
  .event-title span { display: block; }
  .title-main { font-size: 40px; margin-bottom: 10px; }
  .title-join { font-size: 36px; font-weight: 400; margin-bottom: 10px; }
  .title-big { font-size: 46px; margin-bottom: 8px; }
  .save-block {
    position: absolute; top: 450px; left: 90px; width: 450px; height: 170px;
  }
  .save-words {
    position: absolute; left: 0; top: 0;
    font: 400 86px/1 "Amatic SC", sans-serif; color: var(--navy); letter-spacing: -.02em;
  }
  .save-date {
    position: absolute; left: 0; top: 70px;
    font: 500 110px/1 "Cormorant SC", serif; color: var(--crimson);
  }
  .date-stack {
    position: absolute; right: 0; top: 6px; text-align: center;
    font: 400 46px/1 "Cormorant SC", serif; color: var(--navy);
  }
  .date-stack .day { display: block; font-size: 74px; color: var(--crimson); line-height: .95; }
  .date-stack .month, .date-stack .year { display: block; }
  .venue {
    position: absolute; top: 655px; width: 100%;
    font: 700 19px/1 "Cinzel", serif; color: var(--navy);
  }
  .city {
    position: absolute; top: 680px; width: 100%;
    font: 400 15px/1 "Cinzel", serif; color: var(--ink);
  }
  .host-name {
    position: absolute; top: 738px; width: 100%;
    font: 700 19px/1 "Cinzel", serif; color: var(--navy);
    text-transform: uppercase; letter-spacing: .06em;
  }
</style>
</head>
<body>
  <article class="flyer">
    <div class="watercolor-wash" role="img" aria-label="Pink and violet watercolour wash across the top of the flyer"></div>
    <div class="frame" aria-hidden="true"></div>
    <div class="content">
      <p class="invite-line">Have the pleasure of inviting you to our</p>
      <p class="edition">4th Annual</p>
      <h1 class="event-title">
        <span class="title-main">Build With Sisters</span>
        <span class="title-join">And</span>
        <span class="title-big">See Them</span>
        <span class="title-big">Soar!</span>
      </h1>
      <div class="save-block">
        <p class="save-words">Save The</p>
        <p class="save-date">Date</p>
        <p class="date-stack"><span class="month">Jan</span><span class="day">25</span><span class="year">2019</span></p>
      </div>
      <p class="venue">Larkhaven Ridge Resort and Spa</p>
      <p class="city">San Marcos, TX</p>
      <p class="host-name">Q-MarTO</p>
    </div>
  </article>
</body>
</html>
```